2 banner Designs

I have a trade show in Vegas and I want you to design 2 banners that are Graphic size: 33.5" (W) x 80.5" (H). The banners are standing in the booth.

I am looking for a luxury modern feel for the banners. The banners are going to be important to attract customers in.

I am showing latex foam pillows and latex mattress. The company is called Verdant Rest. Please use any photos from our website.

https://www.lumivaslee.net/verdantrest

Banner 1

Introducing our Verdant Rest mattress, a perfect harmony of luxurious organic cushioning and an advanced internal, zoned pressure-point support system.

Experience unparalleled back support and remarkable durability, all in one exceptional sleep solution.

Verdant Rest Mattress

HVRA-certified organic cotton
HVRA-certified organic wool
2 “ HVLA-certified organic latex
8” Pocket Coils
1’’ HVLA-certified organic latex

Banner 2

Verdant Rest Pillows

We developed a customizable pillow with the perfect amount of comfort and support.

Our New Latex pillow has an adjustable fill with 90% Natural Latex and 10% Traceable Wool.  Our pillow cover is made from HVRA-certified organic cotton.

FILE REQUIREMENTS
We can take the file in the following file formats:

Single Page PDF (Preferred)
JPG (Preferred)
PSD – Please flatten file
EPS – Please embed all images. Outline all fonts and strokes.
Ai – Please embed all images. Outline all fonts and strokes.
Don't Include Crop Marks or Bleed

Artwork at either full scale, 1/2 scale or 1/10 scale that is fine. Just make sure that when the file is being set up the DPI is compensated according to the scale.

Full Scale – 150 DPI
1/2 Scale – 300 DPI
1/10 Scale – 450 DPI
***Remove EVERYTHING from your file that you do not want printed on the final product - especially hidden layers and template guidelines.

- Flatten all Objects/Gradients/Swatches/Symbols/Special Effects/Transparencies
- Outline all text
- Flattened PDF (Single Page) or JPEG file types only
- Remove all crop marks/bleed otherwise they will be printed
- File must be the same exact size as what is ordered (exception is Gallery wrap Fold Edge and Products with templates)
- CMYK only (we do not print Pantone/5th/Spot/RGB)
- 150 dpi
- If using a template, the file uploaded to our site should match the exact "template size" (different than "graphic size").
- Do not scale template files, just flatten them and save at 150 dpi
- Files over 200" can be scaled
- Under 300 mb for upload

- Make sure all objects are embedded and flattened (we do not print Non-Native Art).
- If the file is made in Indesign, please flatten the file in Illustrator or Photoshop and export to a JPEG ONLY as we don't recommend using Indesign at our facility.

- If using Compound Paths to create transparencies/shapes, please completely rasterize or flatten them into the file or they may print incorrectly.

- We do not have specific measurements for Panel jobs. If you are printing in Panels, please make sure you are providing a minimum of 1" overlay in your files.

Please make sure that your file is in CMYK format for print production with no bleed. It is not required.

```html
<!DOCTYPE html>
<html lang="en">
<head>
<meta charset="utf-8">
<title>Verdant Rest Pillows – Standing Banner</title>
<link rel="stylesheet" href="https://fonts.googleapis.com/css2?family=Marcellus&family=Montserrat:wght@400;600;700&display=swap">
<style>
  :root {
    --page-bg: #c9c9c9;
    --paper: #ffffff;
    --leaf-green: #6a9e2c;
    --green-light: #93c447;
    --green-mid: #76aa33;
    --green-deep: #5a8c20;
    --photo-warm: #e9dccd;
    --photo-cool: #d8d6d0;
    --photo-skin: #d79a7d;
    --ink: #3a3a3a;
  }
  * { margin: 0; padding: 0; box-sizing: border-box; }
  html, body {
    width: 1200px; height: 948px; overflow: hidden;
    background: var(--page-bg);
  }
  .banner {
    position: absolute; left: 412px; top: 24px;
    width: 375px; height: 900px;
    background: var(--paper);
    overflow: hidden;
    box-shadow: 0 10px 30px rgba(0,0,0,.18);
    font-family: "Montserrat", sans-serif;
  }
  .banner__art { position: absolute; inset: 0; }
  .brand {
    position: absolute; left: 0; right: 0; top: 120px;
    text-align: center; color: var(--leaf-green);
    font-family: "Marcellus", serif; font-weight: 400;
    font-size: 36px; letter-spacing: 2px; text-transform: uppercase;
    line-height: 1.05;
  }
  .intro {
    position: absolute; left: 23px; top: 444px; width: 170px;
    color: #fff; font-size: 13px; line-height: 20px; font-weight: 400;
  }
  .intro strong { font-weight: 700; }
  .headline {
    position: absolute; left: 0; right: 0; top: 582px;
    text-align: center; color: #fff;
    font-size: 19.5px; line-height: 28px; font-weight: 700;
  }
  .web {
    position: absolute; left: 0; right: 0; top: 856px;
    text-align: center; color: var(--ink);
    font-size: 18px; font-weight: 400;
  }
  .web strong { color: var(--leaf-green); font-weight: 700; }
</style>
</head>
<body>
<main class="banner">
  <svg class="banner__art" width="375" height="900" viewBox="0 0 375 900" aria-hidden="false">
    <defs>
      <linearGradient id="fieldGreen" x1="0" y1="0" x2="0.4" y2="1">
        <stop offset="0" stop-color="var(--green-light)"/>
        <stop offset="0.5" stop-color="var(--green-mid)"/>
        <stop offset="1" stop-color="var(--green-deep)"/>
      </linearGradient>
      <linearGradient id="photoBed" x1="0" y1="0" x2="1" y2="1">
        <stop offset="0" stop-color="#f1ebe2"/>
        <stop offset="1" stop-color="#c79a74"/>
      </linearGradient>
      <linearGradient id="photoSofa" x1="0" y1="0" x2="1" y2="1">
        <stop offset="0" stop-color="#e6e3dc"/>
        <stop offset="1" stop-color="#b9b7b2"/>
      </linearGradient>
      <linearGradient id="photoFill" x1="0" y1="0" x2="1" y2="1">
        <stop offset="0" stop-color="#ece7e0"/>
        <stop offset="1" stop-color="var(--photo-skin)"/>
      </linearGradient>
    </defs>

    <!-- green field with cut-out for the photo cluster -->
    <path class="green-field" fill="url(#fieldGreen)"
      d="M0,300 C0,365 40,402 105,402 L192,402 L192,470
         C192,525 232,565 292,565 L375,565 L375,808
         C320,780 262,790 190,812 C115,836 55,812 0,800 Z"/>

    <!-- photo tiles -->
    <g class="photo-cluster" stroke="var(--leaf-green)" stroke-width="3.5">
      <path fill="none" d="M16,199 L150,199 Q213,199 213,262 L213,384 L80,384 Q16,384 16,320 Z"/>
      <path role="img" aria-label="Photo: woman sitting on a bed hugging a latex pillow" stroke="none"
        fill="url(#photoBed)" d="M22,205 L150,205 Q207,205 207,262 L207,378 L80,378 Q22,378 22,320 Z"/>

      <path fill="none" d="M204,237 L304,237 Q363,237 363,296 L363,398 L204,398 Z"/>
      <path role="img" aria-label="Photo: man resting on a sofa with his pillow" stroke="none"
        fill="url(#photoSofa)" d="M210,243 L304,243 Q357,243 357,296 L357,392 L210,392 Z"/>

      <path fill="none" d="M204,398 L363,398 L363,480 Q363,545 298,545 L204,545 Z"/>
      <path role="img" aria-label="Photo: hands adjusting the pillow's latex fill" stroke="none"
        fill="url(#photoFill)" d="M210,404 L357,404 L357,480 Q357,539 298,539 L210,539 Z"/>
    </g>

    <!-- certification badge as plain mark -->
    <circle class="cert-badge" cx="187" cy="763" r="44" fill="none" stroke="#ffffff" stroke-width="3"/>
    <circle cx="187" cy="763" r="30" fill="rgba(255,255,255,.18)"/>
  </svg>

  <h1 class="brand">Verdant Rest</h1>

  <p class="intro"><strong>We developed a customizable pillow</strong> with the perfect amount of <strong>comfort</strong> and <strong>support.</strong></p>

  <p class="headline">Our New Latex pillow<br>has an adjustable fill with<br>90% Natural Latex and 10%<br>Traceable Wool.</p>

  <p class="web">www.<strong>lumivaslee</strong>.net</p>
</main>
</body>
</html>
```